Yacht, Boats, Watersports company needs a redesign of business card

Hello Designers!
We are a Boat dealership company that sells fun in the water, we sell boats, Yachts, Kayaks and also yacht WaterSport toys. We are looking to redesign our business cards in to something a little bit more sophisticated. in a way that we can make better use of our company colors. I'm attaching a zipped file containing the company 3 sets of company logo which one is an horizontal another one is a vertical and also a chromed 3d logo. Also is included two set of business cards that we use and also some designs that i think it's interesting. We use PMS 2026c Orange and PMS 7687C Blue. I would like to see at least two different options with the orange as accent and also using blue as an accent color. It's really important for the business cards to have a font option and size that is legible to most people. Our current website is wwww.corvellamarine.com. Please visit if you want to have a better feeling of the Boat dealership
You can send Single sided or double side options. We are now using single sided but we may be open for a double side option if we really like the design.
Target Market(s)
Marine, boat sales, yacht sales, water toys sales/
Contact Information for Business Card
Name: Dale Pritchett
Address: 718 West Halden Lane,
Dania Beach, FL 33019
Phone: 954-382-7146
Fax: 954:382-7139
Cell: 954-451-8320
Email: 212@corvellamarine.com
Website: corvellamarine.com
Requirements
Must have
- the current information of the business card provided.
logo
use the PMS Colors
Nice to have
- a touch of elegance and sophistication but simple
Should not have
- should not have any typography that is hard to read, the card should be simple but yet sophisticated.

```html
<!DOCTYPE html>
<html lang="en">
<head>
<meta charset="UTF-8">
<title>Corvella Marine – Business Card</title>
<link href="https://fonts.googleapis.com/css2?family=Montserrat:wght@400;500;700;800&display=swap" rel="stylesheet">
<style>
  :root {
    --backdrop: #e8e8e8;
    --card-white: #ffffff;
    --brand-orange: #f26b2f;
    --brand-navy: #1d3f7c;
    --brand-blue: #0556a6;
    --text-grey: #5f5f5f;
    --rule-grey: #6b6b6b;
    --on-blue: #ffffff;
  }
  * { box-sizing: border-box; margin: 0; padding: 0; }
  html, body { width: 1200px; height: 800px; overflow: hidden; }
  body {
    background: var(--backdrop);
    font-family: "Montserrat", Arial, sans-serif;
    position: relative;
  }
  .card {
    position: absolute;
    top: 245px;
    width: 540px;
    height: 310px;
    border-radius: 18px;
    box-shadow: 0 12px 30px rgba(0,0,0,0.15);
    overflow: hidden;
  }

  /* Front */
  .card-front { left: 40px; background: var(--card-white); }
  .brand-lockup {
    position: absolute;
    right: 60px;
    top: 62px;
    display: flex;
    align-items: center;
    gap: 10px;
  }
  .brand-dot {
    width: 30px; height: 30px;
    border-radius: 50%;
    background: var(--brand-orange);
  }
  .brand-name {
    font-weight: 800;
    font-size: 24px;
    letter-spacing: 1px;
    text-transform: uppercase;
    color: var(--brand-navy);
  }
  .person {
    position: absolute;
    left: 40px;
    top: 118px;
  }
  .person-name {
    font-weight: 700;
    font-size: 22px;
    line-height: 1;
    white-space: nowrap;
  }
  .person-name .first { color: var(--brand-orange); }
  .person-name .last { color: var(--brand-navy); }
  .person-title {
    font-size: 13px;
    color: var(--text-grey);
    margin-top: 4px;
  }
  .divider {
    position: absolute;
    left: 214px;
    right: 40px;
    top: 138px;
    height: 1.5px;
    background: var(--rule-grey);
  }
  .contact-list {
    position: absolute;
    left: 56px;
    top: 178px;
    list-style: none;
  }
  .contact-list li {
    display: flex;
    align-items: center;
    gap: 8px;
    font-size: 13px;
    line-height: 19px;
    color: var(--text-grey);
  }
  .contact-icon { width: 12px; height: 12px; flex: none; }
  .address {
    position: absolute;
    right: 40px;
    top: 166px;
    font-style: normal;
    font-size: 13px;
    line-height: 19px;
    color: var(--text-grey);
  }

  /* Back */
  .card-back {
    right: 40px;
    background: var(--brand-blue);
    color: var(--on-blue);
  }
  .back-lockup {
    position: absolute;
    left: 0; right: 0;
    top: 110px;
    display: flex;
    align-items: center;
    justify-content: center;
    gap: 12px;
  }
  .back-lockup .brand-dot {
    width: 34px; height: 34px;
    background: transparent;
    border: 4px solid var(--on-blue);
  }
  .back-lockup .brand-name { color: var(--on-blue); font-size: 28px; }
  .services {
    position: absolute;
    left: 0; right: 0;
    top: 212px;
    display: flex;
    justify-content: center;
    gap: 18px;
    list-style: none;
    font-size: 14px;
    font-weight: 500;
  }
  .services li::before {
    content: "";
    display: inline-block;
    width: 5px; height: 5px;
    border-radius: 50%;
    background: var(--on-blue);
    margin-right: 6px;
    vertical-align: middle;
  }
</style>
</head>
<body>

<section class="card card-front">
  <div class="brand-lockup">
    <span class="brand-dot"></span>
    <span class="brand-name">Corvella Marine</span>
  </div>

  <div class="person">
    <p class="person-name"><span class="first">Dale</span> <span class="last">Pritchett</span></p>
    <p class="person-title">Owner</p>
  </div>

  <div class="divider"></div>

  <ul class="contact-list">
    <li>
      <svg class="contact-icon" viewBox="0 0 12 12" fill="none" stroke="#f26b2f" stroke-width="1.3"><rect x="1" y="2" width="10" height="8" rx="1"/></svg>
      555-382-7146
    </li>
    <li>
      <svg class="contact-icon" viewBox="0 0 12 12" fill="none" stroke="#f26b2f" stroke-width="1.3"><rect x="3" y="1" width="6" height="4"/><rect x="1" y="5" width="10" height="5" rx="1"/></svg>
      555:382-7139
    </li>
    <li>
      <svg class="contact-icon" viewBox="0 0 12 12" fill="#f26b2f"><path d="M2 1h3l1 3-2 1a7 7 0 0 0 3 3l1-2 3 1v3c-5 0-9-4-9-9z"/></svg>
      555-451-8320
    </li>
    <li>
      <svg class="contact-icon" viewBox="0 0 12 12" fill="none" stroke="#f26b2f" stroke-width="1.3"><rect x="1" y="2.5" width="10" height="7"/><path d="M1 2.5l5 4 5-4"/></svg>
      212@corvellamarine.com
    </li>
    <li>
      <svg class="contact-icon" viewBox="0 0 12 12" fill="none" stroke="#f26b2f" stroke-width="1.3"><circle cx="6" cy="6" r="5"/><path d="M1 6h10M6 1c-2.5 3-2.5 7 0 10M6 1c2.5 3 2.5 7 0 10"/></svg>
      wwww.corvellamarine.com
    </li>
  </ul>

  <address class="address">
    718 West Halden Lane,<br>
    Coral Haven, FL 33019
  </address>
</section>

<section class="card card-back">
  <div class="back-lockup">
    <span class="brand-dot"></span>
    <span class="brand-name">Corvella Marine</span>
  </div>
  <ul class="services">
    <li>Marine</li>
    <li>boat sales</li>
    <li>yacht sales</li>
    <li>water toys sales</li>
  </ul>
</section>

</body>
</html>
```